BKA

Please send us some options for letterhead I attached our Logo. In addition to the Logo we need this information somewhere on the page

47 Fenbury Lane
Dunmore, CT 06517
203-481-7629

```html
<!DOCTYPE html>
<html lang="en">
<head>
<meta charset="utf-8">
<title>BKA Letterhead</title>
<link href="https://fonts.googleapis.com/css2?family=Arimo:wght@400;700&display=swap" rel="stylesheet">
<style>
  :root {
    --charcoal: #58595b;
    --brand-dark: #4a3f3c;
    --sky: #4fc3ec;
    --paper: #ffffff;
    --mist: #eceae8;
    --footer-gray: #8c8a8a;
  }
  html, body {
    margin: 0;
    padding: 0;
    overflow: hidden;
    background: var(--paper);
  }
  .letterhead {
    position: relative;
    width: 848px;
    height: 1200px;
    overflow: hidden;
    background: var(--paper);
    font-family: "Arimo", Arial, sans-serif;
  }
  .letterhead svg {
    position: absolute;
    inset: 0;
  }
  .roof { fill: var(--charcoal); }
  .footer-band-gray { fill: var(--footer-gray); }
  .footer-band-blue { fill: var(--sky); }
  .brand {
    position: absolute;
    top: 58px;
    left: 0;
    width: 848px;
    display: flex;
    justify-content: center;
    align-items: center;
    gap: 14px;
  }
  .brand-square {
    width: 30px;
    height: 30px;
    background: var(--sky);
  }
  .brand-name {
    font-weight: 700;
    font-size: 52px;
    letter-spacing: 2px;
    color: var(--brand-dark);
    line-height: 1;
  }
  .brand-ghost {
    position: absolute;
    top: 470px;
    left: 0;
    width: 848px;
    text-align: center;
    font-weight: 700;
    font-size: 230px;
    letter-spacing: 10px;
    color: var(--mist);
    line-height: 1;
  }
  .contact {
    position: absolute;
    margin: 0;
    font-weight: 700;
    color: var(--paper);
    white-space: nowrap;
    line-height: 1;
  }
  .contact-phone {
    left: 164px;
    top: 1145px;
    font-size: 16px;
  }
  .contact-address {
    left: 487px;
    top: 1167px;
    font-size: 17px;
  }
</style>
</head>
<body>
  <div class="letterhead">
    <svg width="848" height="1200" viewBox="0 0 848 1200" aria-hidden="true">
      <path class="roof" d="M0,0 H848 V142 L712,97 V31 H637 V73 L425,3 L0,138 Z"/>
      <path class="footer-band-gray" d="M0,1140 H430 L414,1165 H0 Z"/>
      <rect class="footer-band-blue" x="0" y="1171" width="420" height="5"/>
      <path class="footer-band-blue" d="M412,1200 L440,1156 H848 V1200 Z"/>
    </svg>

    <header class="brand">
      <span class="brand-square"></span>
      <span class="brand-name">BKA</span>
    </header>

    <div class="brand-ghost" aria-hidden="true">BKA</div>

    <p class="contact contact-phone">203-481-7629</p>
    <p class="contact contact-address">47 Fenbury Lane Dunmore, CT 06517</p>
  </div>
</body>
</html>
```